Specialist Technical Theatre service for schools

The task is to design a brochure (A5, 4 pages) for mailing to secondary/high school heads and drama departments to sell them our services as Technical Theatre and Drama professionals who can help them to offer elements of a curriculum that they do not currently offer as well as raise the technical standards of their school productions.
Please find a document attached which outlines the content for the brochure. Please read the document first so that you understand our aims. The text highlighted in yellow takes priority - the text highlighted in blue could be used if there is space.
Photos which may be used available on https://www.pictaro.com/photos/ben_tovey/ (please do not use watermarked nordel images).
Logo is attached (two variants) - one of which should appear somewhere on the design. Website address is www.bentovey.co.uk and email is info@bentovey.co.uk
Target Market(s)
Theatre and Drama teachers in Secondary/High schools
Headteachers of Secondary/High Schools
Industry/Entity Type
Education
Look and feel

```html
<!DOCTYPE html>
<html lang="en">
<head>
<meta charset="utf-8">
<title>Ben Tovey – Technical Theatre for Schools</title>
<link rel="stylesheet" href="https://fonts.googleapis.com/css2?family=Marcellus&display=swap">
<style>
  :root {
    --page: #ffffff;
    --ink: #2a2a2a;
    --ink-soft: #9a9a9a;
    --ink-faint: #b0b0b0;
    --navy: #232a44;
    --gold: #8a6f3c;
    --band: #1b1712;
    --shadow: rgba(0,0,0,0.35);
  }
  html, body {
    margin: 0;
    width: 1200px;
    height: 1000px;
    overflow: hidden;
    background: var(--page);
    font-family: "Marcellus", Georgia, serif;
    color: var(--ink);
  }
  .spread {
    position: absolute;
    left: 42px; top: 106px;
    width: 1115px; height: 787px;
    background: var(--page);
    box-shadow: 0 4px 14px var(--shadow);
    overflow: hidden;
  }
  .block { position: absolute; }
  .intro { left: 29px; top: 36px; width: 490px; }
  .intro p {
    margin: 0;
    font-size: 13.5px;
    line-height: 21px;
    text-align: justify;
  }
  .intro .source {
    margin-top: 4px;
    font-size: 10px;
    color: var(--ink-faint);
  }
  .group-list {
    left: 60px; top: 150px; width: 489px;
    margin: 0; padding: 0; list-style: none;
    font-size: 13px; line-height: 21px;
    color: var(--ink-soft);
    text-align: justify;
  }
  .photo-dancer {
    left: 0; top: 341px; width: 557px; height: 358px;
    background: radial-gradient(ellipse at 80% 60%, #b0189a 0%, #5a0c55 25%, transparent 50%),
                radial-gradient(ellipse at 45% 55%, #6a4a3a 0%, #2a1a18 40%, #0a0608 80%);
  }
  .caption-bar {
    left: 0; top: 341px; width: 557px; height: 52px;
    background: rgba(20,16,22,0.72);
  }
  .caption-bar p {
    margin: 8px 29px 0;
    color: #ffffff;
    font-size: 12.5px;
    line-height: 19px;
  }
  .photo-stage {
    left: 557px; top: 0; width: 558px; height: 274px;
    background: radial-gradient(ellipse at 50% 15%, #dfe6ee 0%, #7d8a99 25%, #27313d 55%, #0d1218 85%);
  }
  .pitch { left: 585px; top: 292px; width: 488px; }
  .pitch p {
    margin: 0;
    font-size: 13.5px;
    line-height: 21px;
    text-align: justify;
  }
  .pitch .answer { font-size: 12.5px; }
  .credentials {
    left: 585px; top: 444px; width: 488px;
    margin: 0; padding: 0; list-style: none;
    font-size: 12.5px; line-height: 21px;
    text-align: justify;
  }
  .credentials li {
    position: relative;
    padding-left: 28px;
  }
  .credentials li::before {
    content: "";
    position: absolute;
    left: 0; top: 3px;
    width: 14px; height: 14px;
    border-radius: 50%;
    background: var(--navy);
  }
  .footer-band {
    left: 0; top: 699px; width: 1115px; height: 57px;
    background: linear-gradient(to bottom, var(--band) 0%, #2b241b 50%, var(--band) 100%);
    border-top: 2px solid var(--gold);
    border-bottom: 2px solid var(--gold);
    box-sizing: border-box;
  }
  .brand-mark {
    width: 76px; height: 76px;
    top: 689px;
    border-radius: 50%;
    background: var(--navy);
    display: flex; align-items: center; justify-content: center;
    text-align: center;
    color: #ffffff;
    font-size: 15px;
    line-height: 17px;
  }
  .brand-left { left: 248px; }
  .brand-right { left: 805px; }
</style>
</head>
<body>
<div class="spread">
  <div class="block intro">
    <p>With 60% of marks being allocated to the practical elements of ‘creating original drama’ and ‘making theatre’ you would like to offer your students the opportunity to pursue the technical design elements of the course but don’t have the technical support?</p>
    <p class="source">Arden A-level Drama and Theatre and Exbridge GCSE Drama (from September 2016)</p>
  </div>

  <ul class="block group-list">
    <li>A GCSE or A-Level performance group can comprise of:</li>
    <li>Directing (one candidate per group)</li>
    <li>Acting (at least two candidates per group)</li>
    <li>Costume design (one candidate per group)</li>
    <li>Mask design (one candidate per group)</li>
    <li>Set design (one candidate per group)</li>
    <li>Technical elements: Lighting and/or Sound (one candidate per element or one candidate assuming responsibility for both elements)</li>
  </ul>

  <div class="block photo-dancer" role="img" aria-label="Photo of a dancer performing under magenta stage light"></div>
  <div class="block caption-bar">
    <p>You would like someone with the specialist knowledge to ensure that your students meet the assessment criteria?</p>
  </div>

  <div class="block photo-stage" role="img" aria-label="Photo of a cast in silhouette on a smoky stage under spotlights"></div>

  <div class="block pitch">
    <p>Your school and Drama Department owns a wide range of technical theatre equipment that isn’t used to its full potential?</p>
    <p>You have a school wide musical, play or dance performance approaching and would like to get a student crew motivated, trained and involved in the technical aspects of the performance?</p>
    <p class="answer">If your answer to any of the above is ‘yes’ then we can help.</p>
  </div>

  <ul class="block credentials">
    <li>SCS checked staff (subscribed to the SCS update service so you can run an instant check on our arrival)</li>
    <li>Qualified in Technical Theatre (through a Stage Schools Guild accredited establishment)</li>
    <li>ISHP certified (we adopt the latest safe working practice)</li>
    <li>First Aid Qualified (just in case!)</li>
    <li>Experience of working with Children and Young People in Education (includes previous experience of teaching production skills to GCSE and A-Level students and Youth theatre)</li>
    <li>Currently working in the Theatre and Events Industry (we bring current industry knowledge to you and your students)</li>
  </ul>

  <div class="block footer-band" role="img" aria-label="Dark decorative footer band"></div>
  <div class="block brand-mark brand-left">Ben<br>Tovey</div>
  <div class="block brand-mark brand-right">Ben<br>Tovey</div>
</div>
</body>
</html>
```